Business Card Design

We sell fish products to corporate food companies who then turn these products into final food products for consumers

Industry/Entity Type

Business

Contact Information for Business Card

I need a corporate business card template for a fish products business. We would like it be professional for use in dealing with multi national companies. This company business card template will be used by multiple employees so the following fields must be open to edit (Name, Phone Number and Email address)

```html
<!DOCTYPE html>
<html lang="en">
<head>
<meta charset="utf-8">
<title>Tidewater Seafoods — Business Card</title>
<link rel="stylesheet" href="https://fonts.googleapis.com/css2?family=Lato:wght@400;700&display=swap">
<style>
  :root {
    --page-bg: #eceef1;
    --card-white: #ffffff;
    --card-grey: #f1f2f4;
    --brand-blue: #1f78c8;
    --deep-blue: #0d5fb0;
    --ocean-blue: #1a72c4;
    --aqua: #4fc0e0;
    --sea-green: #6fcfa8;
    --ink: #333a42;
    --pale-text: #cfe6f7;
  }
  * { margin: 0; padding: 0; box-sizing: border-box; }
  html, body {
    width: 1200px; height: 1022px; overflow: hidden;
    background: var(--page-bg);
    font-family: "Lato", sans-serif;
  }
  .sheet {
    width: 1200px; height: 1022px;
    display: flex; flex-direction: column;
    align-items: center; justify-content: center; gap: 60px;
  }
  .card {
    position: relative;
    width: 700px; height: 400px;
    border-radius: 22px;
    overflow: hidden;
    box-shadow: 0 6px 22px rgba(20, 40, 70, 0.18);
  }

  /* Front */
  .card-front { background: linear-gradient(160deg, var(--card-white) 40%, var(--card-grey)); }
  .card-front .wave-band { position: absolute; inset: 0; }
  .brand-name-front {
    position: absolute; top: 44px; right: 60px;
    font-weight: 400; font-size: 34px; letter-spacing: 1px;
    color: var(--brand-blue); text-align: right; line-height: 1.15;
  }
  .fish-art {
    position: absolute; right: 28px; top: 150px;
    width: 150px; height: 120px; border-radius: 50% 50% 45% 45%;
    background: radial-gradient(circle at 40% 40%, #8fdcbd, var(--sea-green));
  }
  .contact {
    position: absolute; left: 56px; bottom: 58px;
    color: var(--ink);
  }
  .contact .person-name { font-weight: 700; font-size: 24px; color: var(--brand-blue); }
  .contact .person-title { font-size: 17px; margin-top: 4px; }
  .contact .lines { margin-top: 18px; font-size: 17px; }
  .contact .line { display: flex; align-items: center; gap: 10px; margin-top: 6px; }
  .contact svg { width: 16px; height: 16px; fill: var(--brand-blue); }

  /* Back */
  .card-back {
    background: linear-gradient(135deg, #2a86d8 0%, var(--deep-blue) 70%, #0b4f96 100%);
  }
  .brand-name-back {
    position: absolute; left: 62px; top: 70px;
    font-weight: 400; font-size: 52px; letter-spacing: 3px; line-height: 1.1;
    color: var(--pale-text);
  }
  .brand-dot {
    position: absolute; right: 90px; bottom: 70px;
    width: 130px; height: 130px; border-radius: 50%;
    background: rgba(79, 192, 224, 0.55);
  }
</style>
</head>
<body>
<main class="sheet">
  <section class="card card-front">
    <svg class="wave-band" viewBox="0 0 700 400" preserveAspectRatio="none" aria-hidden="true">
      <defs>
        <linearGradient id="bandFill" x1="0" y1="0" x2="1" y2="1">
          <stop offset="0" stop-color="#2f8fdc"/>
          <stop offset="1" stop-color="#0f63b4"/>
        </linearGradient>
      </defs>
      <path d="M300,400 C380,330 470,290 560,275 C620,265 670,262 700,255 L700,400 Z" fill="url(#bandFill)"/>
    </svg>
    <div class="brand-name-front">Tidewater<br>Seafoods</div>
    <div class="fish-art" role="img" aria-label="Green fish illustration"></div>
    <div class="contact">
      <div class="person-name">Marin Alder Grey</div>
      <div class="person-title">Director</div>
      <div class="lines">
        <div class="line">
          <svg viewBox="0 0 24 24"><path d="M6.6 10.8a15.1 15.1 0 0 0 6.6 6.6l2.2-2.2c.3-.3.7-.4 1-.2 1.1.4 2.3.6 3.6.6.6 0 1 .4 1 1V20c0 .6-.4 1-1 1A17 17 0 0 1 3 4c0-.6.4-1 1-1h3.5c.6 0 1 .4 1 1 0 1.3.2 2.5.6 3.6.1.3 0 .7-.2 1z"/></svg>
          <span class="phone">(555) 210 4836</span>
        </div>
        <div class="line">
          <svg viewBox="0 0 24 24"><path d="M2 5h20v14H2zM4 7v.5l8 5 8-5V7zm0 2.9V17h16V9.9l-8 5z"/></svg>
          <span class="email">hello@tidewatermail.com</span>
        </div>
      </div>
    </div>
  </section>

  <section class="card card-back">
    <div class="brand-name-back">Tidewater<br>Seafoods</div>
    <div class="brand-dot"></div>
  </section>
</main>
</body>
</html>
```